Letterhead Design Project

Initially, we would like to review our letterheads.

Something simple which uses our corporate imagery well and is nicely balanced.

Please note that I will be following up this letter-head with some customised quote templates and similarly customisable collateral in the next few weeks.

Target Market(s)

Enterprise business

Industry/Entity Type

Quote

Requirements
Must have
• The Norbix7 logo
See www.norbix7.com.au

Our tagline "Enterprise Hosting, Messaging and Server Virtualisation"

Our website address

Ideally in our colour pallette, but will consider submissions which look fantastic and necessitate other colours.

```html
<!DOCTYPE html>
<html lang="en">
<head>
<meta charset="UTF-8">
<title>Norbix7 Letterhead</title>
<link href="https://fonts.googleapis.com/css2?family=PT+Sans:wght@400;700&display=swap" rel="stylesheet">
<style>
  :root {
    --brand-red: #d3202a;
    --ink: #111111;
    --band-dark: #1c1a1a;
    --paper-top: #ffffff;
    --paper-bottom: #ededed;
    --text-grey: #555555;
    --white: #ffffff;
  }
  * { margin: 0; padding: 0; box-sizing: border-box; }
  html, body { width: 986px; height: 1200px; overflow: hidden; background: #f4f4f4; }
  .letterhead {
    position: relative;
    width: 986px;
    height: 1200px;
    background: linear-gradient(160deg, var(--paper-top) 30%, var(--paper-bottom) 100%);
    font-family: "PT Sans", Arial, sans-serif;
    overflow: hidden;
  }
  .header-band {
    position: absolute;
    top: 30px; left: 0;
    width: 986px; height: 66px;
    display: flex;
  }
  .header-band__fade {
    width: 108px;
    background: linear-gradient(90deg, #8a8a8a 0%, #2a2a2a 70%, var(--band-dark) 100%);
  }
  .brand {
    width: 371px;
    background: var(--white);
    display: flex;
    align-items: center;
    padding-left: 11px;
    gap: 14px;
  }
  .brand__square {
    width: 70px; height: 66px;
    background: var(--brand-red);
  }
  .brand__name {
    font-weight: 700;
    font-size: 64px;
    line-height: 1;
    color: var(--ink);
    letter-spacing: -1px;
  }
  .tagline {
    flex: 1;
    background: linear-gradient(90deg, #000 0%, var(--band-dark) 40%, #3a3636 100%);
    color: var(--white);
    font-size: 20px;
    display: flex;
    align-items: center;
    padding-left: 12px;
    white-space: nowrap;
  }
  .tagline__sep { margin: 0 9px; opacity: 0.9; }
  .contact {
    position: absolute;
    left: 28px;
    top: 1130px;
    font-size: 15px;
    color: var(--text-grey);
    line-height: 25px;
  }
  .contact__line { display: flex; align-items: center; gap: 6px; }
  .contact__icon { width: 14px; height: 14px; fill: var(--text-grey); }
  .contact__gap { margin-left: 10px; }
  .contact__divider { margin: 0 8px; color: #999; }
  .footer-bar { position: absolute; left: 0; bottom: 0; width: 986px; height: 42px; }
  .footer-web {
    position: absolute;
    right: 22px; bottom: 16px;
    color: var(--white);
    font-size: 20px;
    letter-spacing: 1.5px;
  }
</style>
</head>
<body>
  <div class="letterhead">
    <header class="header-band">
      <div class="header-band__fade"></div>
      <div class="brand">
        <div class="brand__square"></div>
        <span class="brand__name">Norbix7</span>
      </div>
      <div class="tagline">Enterprise Hosting<span class="tagline__sep">|</span>Messaging<span class="tagline__sep">|</span>Server Virtualisation</div>
    </header>

    <footer>
      <div class="contact">
        <div class="contact__line">
          <svg class="contact__icon" viewBox="0 0 24 24" aria-hidden="true"><path d="M6.6 10.8c1.4 2.8 3.8 5.1 6.6 6.6l2.2-2.2c.3-.3.7-.4 1-.2 1.1.4 2.3.6 3.6.6.6 0 1 .4 1 1V20c0 .6-.4 1-1 1C10.6 21 3 13.4 3 4c0-.6.4-1 1-1h3.5c.6 0 1 .4 1 1 0 1.3.2 2.5.6 3.6.1.3 0 .7-.2 1l-2.3 2.2z"/></svg>
          <span>+61 3 9400 7120</span>
          <svg class="contact__icon contact__gap" viewBox="0 0 24 24" aria-hidden="true"><path d="M2 6h20v12H2z M2 6l10 7 10-7" fill="none" stroke="#555" stroke-width="2"/></svg>
          <span>info@norbix7.com.au</span>
        </div>
        <div class="contact__line">
          <span>Norbix7 Pty. Ltd.</span><span class="contact__divider">|</span><span>Suite 4, Level 3, 18 Larkin Parade, Berwick Vale, Australia, VIC - 3811</span>
        </div>
      </div>
      <svg class="footer-bar" viewBox="0 0 986 42" aria-hidden="true">
        <polygon points="0,22 705,22 705,42 0,42" fill="#111"/>
        <polygon points="728,0 986,0 986,42 692,42" fill="#d3202a"/>
      </svg>
      <div class="footer-web">www.norbix7.com.au</div>
    </footer>
  </div>
</body>
</html>
```